Brantmoor FD Recruitment

We are a volunteer fire/EMS department located in New York. We are starting a recruitment campaign for 2020 and will be making signs(approx 30x20) to hang around town with our new graphic from pixel bazaar.

Looking forward to this awesome project!!!

Font styles to use
Sans Serif

Colors
ec1f27
fbed22
ffffff

Requirements
Must have
• There are some specific text that need to be included and in BOLD.
• Top Line: Volunteer With The Brantmoor Fire Department
• Bottom portion : Contact US at www.brantmoorfd.org
• In addition we would like it to see in big & BOLD
• "FREE TRAINING"
• to become
• a FIREFIGHTER OR EMT/MEDIC
• We would also like to see a star of life and a fire dept maltese cross.

```html
<!DOCTYPE html>
<html lang="en">
<head>
<meta charset="utf-8">
<title>Brantmoor FD Recruitment Sign</title>
<link rel="stylesheet" href="https://fonts.googleapis.com/css2?family=Oswald:wght@500;600&family=Passion+One:wght@700&display=swap">
<style>
  :root {
    --page: #ffffff;
    --ember-dark: #1e0d05;
    --ember-mid: #7a3310;
    --ember-glow: #e0701c;
    --band-orange: #e77b1e;
    --headline: #ffffff;
    --accent-yellow: #fbed22;
    --contact-red: #a3282d;
    --cross-red: #ec1f27;
    --star-blue: #1c5aa8;
  }
  html, body {
    margin: 0;
    width: 1200px;
    height: 1200px;
    overflow: hidden;
    background: var(--page);
  }
  .canvas {
    position: relative;
    width: 1200px;
    height: 1200px;
    background: var(--page);
  }
  .sign {
    position: absolute;
    left: 52px;
    top: 99px;
    width: 1096px;
    height: 732px;
    overflow: hidden;
    background: var(--ember-dark);
  }
  .sign__photo {
    position: absolute;
    inset: 0;
    background:
      radial-gradient(ellipse 40% 60% at 95% 70%, rgba(240,120,30,0.85), transparent 70%),
      radial-gradient(ellipse 50% 40% at 30% 10%, rgba(200,100,30,0.7), transparent 70%),
      radial-gradient(ellipse 30% 70% at 62% 60%, rgba(10,4,2,0.95), transparent 80%),
      linear-gradient(180deg, var(--ember-mid) 0%, #3a1a0a 55%, var(--ember-dark) 100%);
  }
  .sign__band {
    position: absolute;
    left: 0;
    top: 176px;
    width: 760px;
    height: 381px;
    background: linear-gradient(90deg, var(--band-orange) 0%, var(--band-orange) 60%, rgba(231,123,30,0.55) 80%, rgba(231,123,30,0) 100%);
  }
  .intro {
    position: absolute;
    left: 70px;
    top: 50px;
    margin: 0;
    font-family: "Oswald", sans-serif;
    font-weight: 600;
    font-size: 45px;
    line-height: 53px;
    color: var(--accent-yellow);
  }
  .offer {
    position: absolute;
    left: 60px;
    top: 215px;
    margin: 0;
    font-family: "Passion One", sans-serif;
    font-weight: 700;
    color: var(--headline);
    text-transform: uppercase;
  }
  .offer__lead { display: block; font-size: 86px; line-height: 86px; letter-spacing: 2px; }
  .offer__link { display: block; font-size: 30px; line-height: 40px; padding-left: 28px; letter-spacing: 1px; }
  .offer__role { display: block; font-size: 84px; line-height: 82px; padding-left: 10px; letter-spacing: 2px; }
  .brand {
    position: absolute;
    right: 36px;
    top: 70px;
    display: flex;
    align-items: center;
    gap: 10px;
    font-family: "Oswald", sans-serif;
    font-weight: 600;
    font-size: 30px;
    color: var(--headline);
  }
  .brand__dot {
    width: 20px;
    height: 20px;
    border-radius: 50%;
    background: var(--accent-yellow);
  }
  .emblems {
    position: absolute;
    left: 92px;
    top: 597px;
    display: flex;
    gap: 26px;
  }
  .contact {
    position: absolute;
    left: 574px;
    top: 607px;
    width: 522px;
    height: 73px;
    background: linear-gradient(90deg, var(--contact-red) 0%, var(--contact-red) 75%, #7a1e22 100%);
    display: flex;
    align-items: center;
    justify-content: flex-end;
    padding-right: 33px;
    box-sizing: border-box;
    font-family: "Oswald", sans-serif;
    font-weight: 600;
    font-size: 34px;
    color: var(--headline);
  }
</style>
</head>
<body>
<main class="canvas">
  <section class="sign">
    <div class="sign__photo" role="img" aria-label="Firefighter in helmet and breathing apparatus silhouetted against a burning building"></div>
    <div class="sign__band"></div>

    <p class="intro">Volunteer With<br>The Brantmoor Fire Department</p>

    <div class="brand"><span class="brand__dot"></span>Brantmoor FD</div>

    <h1 class="offer">
      <span class="offer__lead">"Free Training"</span>
      <span class="offer__link">To Become</span>
      <span class="offer__role">A Firefighter</span>
      <span class="offer__role">Or EMT/Medic</span>
    </h1>

    <div class="emblems">
      <svg class="emblem emblem--star" width="120" height="120" viewBox="-60 -60 120 120" aria-label="Star of life">
        <g fill="var(--star-blue)" stroke="#ffffff" stroke-width="3">
          <path d="M-11,-56 H11 V-19 L43,-37 L54,-18 L22,0 L54,18 L43,37 L11,19 V56 H-11 V19 L-43,37 L-54,18 L-22,0 L-54,-18 L-43,-37 L-11,-19 Z"/>
        </g>
        <rect x="-2.5" y="-44" width="5" height="88" fill="#ffffff"/>
        <path d="M0,-30 C12,-24 12,-14 0,-10 C-12,-6 -12,4 0,8 C12,12 12,22 0,28" fill="none" stroke="#ffffff" stroke-width="4"/>
      </svg>
      <svg class="emblem emblem--cross" width="116" height="116" viewBox="-58 -58 116 116" aria-label="Fire department cross">
        <path d="M-26,-54 Q0,-42 26,-54 L18,-18 L54,-26 Q42,0 54,26 L18,18 L26,54 Q0,42 -26,54 L-18,18 L-54,26 Q-42,0 -54,-26 L-18,-18 Z" fill="var(--cross-red)"/>
        <path d="M-20,-46 Q0,-37 20,-46 L13,-13 L46,-20 Q37,0 46,20 L13,13 L20,46 Q0,37 -20,46 L-13,13 L-46,20 Q-37,0 -46,-20 L-13,-13 Z" fill="#ffffff"/>
        <circle cx="0" cy="0" r="20" fill="none" stroke="var(--cross-red)" stroke-width="4"/>
        <path d="M0,-14 V14 M-14,0 H14" stroke="var(--cross-red)" stroke-width="4"/>
      </svg>
    </div>

    <div class="contact">Contact US at www.brantmoorfd.org</div>
  </section>
</main>
</body>
</html>
```